Sudden Tides "Lantern Road" New Single Cover

Create cover artwork for the band Sudden Tides' new single "Lantern Road" being released early 2020. Style, font and graphics to be consistent with band's previous releases and overall brand identity. Visit www.suddentidesband.example and our Spotify page https://music.example.net/artist/7QzWpLx3RtVnKd8e2YbHcJ?si=MUrTgKa4PLe7skvWq2AmZd to view our previous releases and overall brand identity. Some examples attached as well. We are looking for someone to work with on future projects as well.

Lyrics are here: https://docs.example.org/document/d/3KTp9wrn_2ZQa8eXb4Lo_fimH7C5m83Jz4Pd70hrtVcA/edit

Music is here: https://audiostream.example.com/suddentides/lantern-road/s-pzkwa

Font styles to use
Sans Serif

Colors

Designer to choose colors to be used in the design.

Requirements
Must have
• Must be consistent with current brand identity and with prior album / single art.

```html
<!DOCTYPE html>
<html lang="en">
<head>
<meta charset="utf-8">
<title>Sudden Tides – Lantern Road</title>
<link rel="stylesheet" href="https://fonts.googleapis.com/css2?family=Josefin+Sans:wght@300;700&display=swap">
<style>
  :root {
    --cover-pink: #f47a8c;
    --title-purple: #8a4a9e;
    --band-purple: #9f4a98;
    --disc-light: #bb4a8a;
    --disc-deep: #a04c93;
  }
  html, body {
    margin: 0;
    padding: 0;
    width: 1200px;
    height: 1200px;
    overflow: hidden;
    background: var(--cover-pink);
  }
  .cover {
    position: relative;
    width: 1200px;
    height: 1200px;
    background: var(--cover-pink);
    font-family: "Josefin Sans", "Helvetica Neue", Arial, sans-serif;
  }
  .single-title {
    position: absolute;
    top: 128px;
    left: 0;
    width: 1200px;
    margin: 0;
    text-align: center;
    font-weight: 300;
    font-size: 112px;
    line-height: 1;
    letter-spacing: 0.16em;
    text-indent: 0.16em;
    color: var(--title-purple);
    white-space: nowrap;
  }
  .cover-art {
    position: absolute;
    left: 345px;
    top: 343px;
    width: 510px;
    height: 510px;
  }
  .band-name {
    position: absolute;
    top: 960px;
    left: 0;
    width: 1200px;
    margin: 0;
    text-align: center;
    font-weight: 700;
    font-size: 92px;
    line-height: 1;
    letter-spacing: 0.1em;
    text-indent: 0.1em;
    color: var(--band-purple);
    white-space: nowrap;
  }
</style>
</head>
<body>
  <main class="cover">
    <h1 class="single-title">LANTERN ROAD</h1>

    <svg class="cover-art" viewBox="0 0 510 510" role="img" aria-label="Circular emblem artwork in purple tones at the centre of the cover">
      <defs>
        <radialGradient id="discGradient" cx="35%" cy="30%" r="80%">
          <stop offset="0%" stop-color="var(--disc-light)"/>
          <stop offset="100%" stop-color="var(--disc-deep)"/>
        </radialGradient>
      </defs>
      <circle cx="255" cy="255" r="255" fill="url(#discGradient)"/>
    </svg>

    <h2 class="band-name">SUDDEN TIDES</h2>
  </main>
</body>
</html>
```